Package design for Mica powder sachets

Our mica powder product comes in two sets of colors, a set of 60 and 35 packed inside sachet bags individually. This project will require two sizes of the packing box , one for the set of 60 and other for 35. We do not have a specific design requirement as long as the design reflects the theme of our product. Box diagram for both sizes is attached together with color chart, content, logo, sachet design and sample of a packaging design we like. The content is the same for both sizes accept for number of colors included.

```html
<!DOCTYPE html>
<html lang="en">
<head>
<meta charset="utf-8">
<title>Birch Studio – Mica Powder Box Lid</title>
<link rel="stylesheet" href="https://fonts.googleapis.com/css2?family=Oswald:wght@500;700&family=Playfair+Display:wght@400&family=Roboto:wght@400&display=swap">
<style>
  :root {
    --lid-black: #0b0b0d;
    --tagline-yellow: #e9f53a;
    --logo-white: #f4f4f4;
    --ribbon-pink: #e8177a;
    --badge-green: #7fe83a;
    --badge-lime: #c8f04a;
    --splash-pink: #e0267e;
    --splash-violet: #6a2aa8;
    --splash-cyan: #1fb6d6;
    --splash-white: #f3dbe8;
  }
  * { margin: 0; padding: 0; box-sizing: border-box; }
  html, body { width: 1200px; height: 840px; overflow: hidden; }
  body { background: var(--lid-black); position: relative; font-family: "Roboto", sans-serif; }

  .lid { position: absolute; inset: 0; background: var(--lid-black); overflow: hidden; }

  .powder-burst {
    position: absolute; left: 300px; top: 150px; width: 880px; height: 640px;
    background:
      radial-gradient(ellipse 28% 30% at 58% 48%, var(--splash-white) 0%, rgba(243,219,232,0) 70%),
      radial-gradient(ellipse 40% 38% at 62% 45%, var(--splash-pink) 0%, rgba(224,38,126,0) 72%),
      radial-gradient(ellipse 30% 34% at 30% 70%, var(--splash-cyan) 0%, rgba(31,182,214,0) 70%),
      radial-gradient(ellipse 42% 40% at 40% 35%, var(--splash-violet) 0%, rgba(106,42,168,0) 72%),
      radial-gradient(ellipse 30% 30% at 85% 80%, #3b2ac0 0%, rgba(59,42,192,0) 70%);
    filter: blur(6px);
  }

  .brand-main {
    position: absolute; left: 380px; top: 130px; width: 460px; text-align: center;
    display: flex; align-items: center; justify-content: center; gap: 18px;
  }
  .brand-main .brand-dot { width: 30px; height: 30px; border-radius: 50%; background: var(--logo-white); }
  .brand-main .brand-name {
    font-family: "Oswald", sans-serif; font-weight: 700; font-size: 78px;
    color: var(--logo-white); letter-spacing: 4px; line-height: 1;
  }

  .tagline {
    position: absolute; left: 250px; top: 300px; width: 720px; text-align: center;
    font-family: "Oswald", sans-serif; font-weight: 500; font-size: 27px;
    color: var(--tagline-yellow); letter-spacing: 0.3px; transform: rotate(-6deg);
  }
  .tagline .sep { display: inline-block; width: 9px; height: 9px; background: var(--tagline-yellow); margin: 0 6px; vertical-align: middle; }

  .uses-list {
    position: absolute; right: 60px; top: 160px; width: 240px;
    font-size: 17px; line-height: 1.15; color: var(--logo-white); text-transform: uppercase;
  }

  .count-flag { position: absolute; left: 190px; top: 560px; width: 520px; height: 150px; }
  .count-flag .ribbon { position: absolute; left: 90px; top: 26px; }
  .count-flag .ribbon-text {
    position: absolute; left: 150px; top: 38px; width: 320px;
    font-family: "Playfair Display", serif; font-size: 26px; line-height: 1.0; color: #ffffff; text-transform: uppercase;
  }
  .count-badge {
    position: absolute; left: 0; top: 0; width: 150px; height: 150px; border-radius: 50%;
    background: radial-gradient(circle at 40% 35%, var(--badge-lime) 0%, var(--badge-green) 60%, #3fae22 100%);
    display: flex; align-items: center; justify-content: center;
    font-family: "Playfair Display", serif; font-size: 78px; color: #111;
  }

  .brand-corner {
    position: absolute; right: 70px; bottom: 90px; display: flex; align-items: center; gap: 10px;
  }
  .brand-corner .brand-dot { width: 14px; height: 14px; border-radius: 50%; background: var(--logo-white); }
  .brand-corner .brand-name {
    font-family: "Oswald", sans-serif; font-weight: 700; font-size: 38px; color: var(--logo-white); letter-spacing: 3px;
  }
</style>
</head>
<body>
<main class="lid">
  <div class="powder-burst" role="img" aria-label="Exploding cloud of pink, violet, cyan and white pigment powder"></div>

  <div class="brand-main">
    <span class="brand-dot"></span>
    <span class="brand-name">Birch Studio</span>
  </div>

  <p class="tagline">
    <span class="sep"></span>MULTI-PURPOSE<span class="sep"></span>COSMETIC GRADE<span class="sep"></span>NON-TOXIC<span class="sep"></span>PREMIUM COLORS
  </p>

  <p class="uses-list">For<br>Epoxy resin, soap<br>Slime<br>Candles<br>Paint<br>And much more</p>

  <div class="count-flag">
    <svg class="ribbon" width="420" height="100" viewBox="0 0 420 100" aria-hidden="true">
      <polygon points="0,0 420,0 395,50 420,100 0,100" fill="var(--ribbon-pink)"/>
    </svg>
    <p class="ribbon-text">Inspiring<br>Mica powder<br>colors</p>
    <div class="count-badge">60</div>
  </div>

  <div class="brand-corner">
    <span class="brand-dot"></span>
    <span class="brand-name">Birch Studio</span>
  </div>
</main>
</body>
</html>
```